Bright Path Attorneys Billboard Design for Personal Injury Law Firm

Need a billboard design that we can use for different versions. 1400px X 400px jpeg or png
I have attached the logo and the attorney for the billboard. Attorney Marla Benning
Here is a link to our current website brightpathlegalgroup.example

HEADLINE: HIT BY A TRUCK?
SUBHEAD: NO FEE. BIG FIGHT.
877-GRANTLY

HEADLINE: ACCIDENT?
SUBHEAD: NO FEE, UNLESS WE WIN!
877-GRANTLY

HEADLINE: BIG TRUCK. BIG CASE.
SUBHEAD: YOU PAY $0 UPFRONT
877-GRANTLY

Target Market(s)

People in Car Accident

Industry/Entity Type

Personal Injury Attorneys

```html
<!DOCTYPE html>
<html lang="en">
<head>
<meta charset="utf-8">
<title>Bright Path Attorneys – Billboard</title>
<link rel="stylesheet" href="https://fonts.googleapis.com/css2?family=Anton&family=Inter:wght@400&family=Montserrat:wght@700;800&display=swap">
<style>
  :root {
    --navy-deep: #0a1427;
    --navy-mid: #0f1d38;
    --navy-light: #15274c;
    --white: #ffffff;
    --green: #5fd649;
    --frame-line: rgba(255,255,255,0.55);
    --photo-top: #6d5a4a;
    --photo-mid: #1a2545;
  }
  html, body {
    margin: 0;
    padding: 0;
    overflow: hidden;
    background: var(--navy-deep);
  }
  .billboard {
    position: relative;
    width: 1200px;
    height: 343px;
    overflow: hidden;
    background: linear-gradient(90deg, var(--navy-deep) 0%, var(--navy-mid) 45%, var(--navy-light) 100%);
    color: var(--white);
  }
  .headline {
    position: absolute;
    left: 50px;
    top: 22px;
    margin: 0;
    font-family: "Anton", "Oswald", sans-serif;
    font-weight: 400;
    font-size: 118px;
    line-height: 1.2;
    letter-spacing: 0.5px;
    white-space: nowrap;
  }
  .subhead {
    position: absolute;
    left: 51px;
    top: 140px;
    margin: 0;
    font-family: "Inter", "Helvetica Neue", Arial, sans-serif;
    font-weight: 400;
    font-size: 52px;
    line-height: 1.2;
    letter-spacing: -0.5px;
    white-space: nowrap;
  }
  .contact-bar {
    position: absolute;
    left: 51px;
    top: 231px;
    width: 885px;
    height: 81px;
    box-sizing: border-box;
    border: 1px solid var(--frame-line);
    border-radius: 20px 0 0 20px;
    border-right: none;
  }
  .contact-bar__divider {
    position: absolute;
    left: 563px;
    top: 0;
    width: 1px;
    height: 100%;
    background: var(--frame-line);
  }
  .phone {
    position: absolute;
    left: 25px;
    top: 0;
    height: 100%;
    display: flex;
    align-items: center;
    font-family: "Montserrat", Arial, sans-serif;
    font-weight: 800;
    font-size: 68px;
    letter-spacing: -1px;
    white-space: nowrap;
  }
  .phone__word { color: var(--green); }
  .firm-name {
    position: absolute;
    left: 606px;
    top: 0;
    height: 100%;
    display: flex;
    align-items: center;
    gap: 8px;
    font-family: "Montserrat", Arial, sans-serif;
    font-weight: 700;
    font-size: 16px;
    color: var(--white);
    white-space: nowrap;
  }
  .firm-name__dot {
    width: 12px;
    height: 12px;
    border-radius: 50%;
    background: var(--green);
  }
  .attorney-photo {
    position: absolute;
    left: 882px;
    top: 12px;
    width: 246px;
    height: 331px;
    border-radius: 120px 120px 0 0;
    background: linear-gradient(180deg, var(--photo-top) 0%, #4a3e3a 35%, var(--photo-mid) 70%, #142042 100%);
  }
</style>
</head>
<body>
  <main class="billboard">
    <h1 class="headline">HIT BY A TRUCK?</h1>
    <p class="subhead">No Fee Unless We Win.</p>

    <div class="contact-bar">
      <div class="phone">877-<span class="phone__word">GRANTLY</span></div>
      <div class="contact-bar__divider"></div>
      <div class="firm-name"><span class="firm-name__dot"></span>Bright Path Attorneys</div>
    </div>

    <div class="attorney-photo" role="img" aria-label="Portrait of attorney Marla Benning in a navy blazer, arms crossed"></div>
  </main>
</body>
</html>
```